Criação de Papelaria Profissional para Beleza
A empresa queria:
" Atendemos clientes adultos masculino, feminino, adolescentes para tratamentos estéticos diversos como acne, rejuvenescimento facial, redução de medidas faciais e corporais, depilação, tratamento de celulite, estrias, medicina capilar, laser, cicatrizes, manchas, melasma, pequenos vasos, poros dilatados, limpeza de pele "

```html
<!DOCTYPE html>
<html lang="pt-BR">
<head>
<meta charset="utf-8">
<title>Lumera Clínica Estética — Papel Timbrado</title>
<link href="https://fonts.googleapis.com/css2?family=Raleway:wght@400;500;600&display=swap" rel="stylesheet">
<style>
  :root {
    --navy: #1d3a57;
    --teal: #0e8a80;
    --teal-light: #16a597;
    --teal-dark: #0a5f5a;
    --ink: #3b4450;
    --rule: #1f2a36;
    --paper: #ffffff;
    --mist: #e3e3e3;
    --backdrop: #f2f2f2;
  }
  * { margin: 0; padding: 0; box-sizing: border-box; }
  html, body {
    width: 1200px; height: 1200px; overflow: hidden;
    background: var(--backdrop);
    font-family: "Raleway", sans-serif;
  }
  .letterhead {
    position: absolute; left: 135px; top: 40px;
    width: 930px; height: 1120px;
    background: var(--paper);
    overflow: hidden;
  }
  .artwork-area {
    position: absolute; left: 470px; top: 140px;
    width: 460px; height: 930px;
    background: linear-gradient(90deg, rgba(227,227,227,0) 0%, rgba(227,227,227,0.55) 55%, var(--mist) 100%);
  }
  .brand {
    position: absolute; left: 112px; top: 30px;
    display: flex; align-items: center; gap: 14px;
  }
  .brand-dot {
    width: 26px; height: 26px; border-radius: 50%;
    background: var(--teal);
  }
  .brand-name {
    font-size: 46px; font-weight: 500; letter-spacing: 1px;
    color: var(--navy); line-height: 1; text-transform: uppercase;
  }
  .brand-tagline {
    position: absolute; left: 152px; top: 84px;
    font-size: 15px; font-weight: 600; letter-spacing: 2.4px;
    color: var(--teal); text-transform: uppercase;
  }
  .header-rule {
    position: absolute; left: 400px; top: 70px;
    width: 516px; height: 2px; background: var(--rule);
  }
  .footer-rule {
    position: absolute; top: 1082px; height: 3px; background: var(--rule);
  }
  .footer-rule.left { left: 66px; width: 70px; }
  .footer-rule.right { left: 812px; width: 104px; }
  .contact {
    position: absolute; top: 1066px; left: 150px;
    display: flex; align-items: center; gap: 22px;
    font-size: 11.5px; color: var(--ink); line-height: 1.35;
  }
  .contact-item { display: flex; align-items: center; gap: 8px; white-space: nowrap; }
  .contact-item svg { width: 17px; height: 17px; flex: none; }
  .footer-band {
    position: absolute; left: 0; bottom: 0; width: 100%; height: 20px;
    background: linear-gradient(90deg, var(--teal-dark), var(--teal-light) 55%, var(--teal));
  }
</style>
</head>
<body>
  <main class="letterhead">
    <div class="artwork-area" role="img" aria-label="Área para arte decorativa de faixas curvas em tons de cinza claro"></div>

    <header>
      <div class="brand">
        <span class="brand-dot"></span>
        <span class="brand-name">Lumera</span>
      </div>
      <div class="brand-tagline">Clínica Estética</div>
      <div class="header-rule"></div>
    </header>

    <footer>
      <div class="footer-rule left"></div>
      <div class="contact">
        <div class="contact-item">
          <svg viewBox="0 0 20 20"><circle cx="10" cy="10" r="9.5" fill="var(--rule)"/><path d="M10 4.5a3.5 3.5 0 0 0-3.5 3.5c0 2.6 3.5 7 3.5 7s3.5-4.4 3.5-7A3.5 3.5 0 0 0 10 4.5Z" fill="#fff"/><circle cx="10" cy="8" r="1.3" fill="var(--rule)"/></svg>
          <span>Seu endereço - Bairro<br>Cidade - Estado - CEP 000-0000</span>
        </div>
        <div class="contact-item">
          <svg viewBox="0 0 20 20"><circle cx="10" cy="10" r="8.8" fill="none" stroke="var(--rule)" stroke-width="1.6"/><path d="M7.3 5.8l1.6 2-0.8 1.2c.6 1.2 1.6 2.2 2.8 2.8l1.2-.8 2 1.6-1 1.6c-3.4-.4-6.4-3.4-6.8-6.8Z" fill="var(--rule)"/></svg>
          <span>(00) xxxx-xxxx</span>
        </div>
        <div class="contact-item">
          <svg viewBox="0 0 20 20"><circle cx="10" cy="10" r="8.8" fill="none" stroke="var(--rule)" stroke-width="1.6"/><circle cx="10" cy="10" r="4.5" fill="none" stroke="var(--rule)" stroke-width="1.2"/><ellipse cx="10" cy="10" rx="1.8" ry="4.5" fill="none" stroke="var(--rule)" stroke-width="1"/><line x1="5.5" y1="10" x2="14.5" y2="10" stroke="var(--rule)" stroke-width="1"/></svg>
          <span>www.seusite.com.br</span>
        </div>
        <div class="contact-item">
          <svg viewBox="0 0 20 20"><circle cx="10" cy="10" r="8.8" fill="none" stroke="var(--rule)" stroke-width="1.6"/><circle cx="10" cy="10" r="2.2" fill="none" stroke="var(--rule)" stroke-width="1.4"/><path d="M12.2 8v3c0 1.3 2.2 1.3 2.2-1A4.4 4.4 0 1 0 12 13.8" fill="none" stroke="var(--rule)" stroke-width="1.4"/></svg>
          <span>seuemail@email.com</span>
        </div>
      </div>
      <div class="footer-rule right"></div>
      <div class="footer-band"></div>
    </footer>
  </main>
</body>
</html>
```